Sleek business card design for digital agency.

Brief document attached for detailed description and inspiration. Looking for a minimalist sleek, cool, modern business card design.

Industry/Entity Type

Digital

```html
<!DOCTYPE html>
<html lang="en">
<head>
<meta charset="utf-8">
<title>Flint Studio – Business Card</title>
<link rel="stylesheet" href="https://fonts.googleapis.com/css2?family=Open+Sans:wght@300;400;600&display=swap">
<style>
  :root {
    --stage: #1c1c1d;
    --card-light: #ecebe9;
    --card-dark: #3b3b3c;
    --card-dark-edge: #2e2e2f;
    --ink: #2a2a2a;
    --ink-soft: #5a5a5a;
    --rule: #9a9a9a;
    --gloss: #1e1e1f;
  }
  * { box-sizing: border-box; margin: 0; padding: 0; }
  html, body {
    width: 1200px; height: 900px; overflow: hidden;
    background: var(--stage);
    font-family: "Open Sans", Arial, sans-serif;
  }
  .stage {
    width: 1200px; height: 900px;
    display: flex; flex-direction: column; align-items: center; justify-content: center;
    gap: 60px;
  }
  .card {
    width: 560px; height: 320px;
    position: relative;
    box-shadow: 0 14px 40px rgba(0,0,0,.55);
  }

  /* Back: contact side */
  .card-back { background: var(--card-light); color: var(--ink); }
  .back-brand {
    position: absolute; top: 30px; left: 0; right: 0;
    display: flex; justify-content: center; align-items: center; gap: 10px;
  }
  .brand-dot { width: 18px; height: 18px; border-radius: 50%; background: var(--ink); }
  .brand-name { font-weight: 600; font-size: 22px; letter-spacing: .5px; color: var(--ink); }
  .person { position: absolute; left: 40px; top: 120px; }
  .person-name { font-weight: 400; font-size: 30px; line-height: 1.1; }
  .person-role { font-weight: 300; font-size: 26px; line-height: 1.15; color: var(--ink-soft); }
  .contact-row {
    position: absolute; left: 40px; right: 40px; bottom: 34px;
    display: flex; font-size: 11px; font-weight: 400; color: var(--ink-soft); line-height: 1.9;
  }
  .contact-group { padding: 0 18px; border-left: 1px solid var(--rule); }
  .contact-group:first-child { padding-left: 0; border-left: none; }

  /* Front: brand side */
  .card-front {
    background: linear-gradient(160deg, #454546 0%, var(--card-dark) 45%, var(--card-dark-edge) 100%);
  }
  .front-brand {
    position: absolute; inset: 0;
    display: flex; align-items: center; justify-content: center; gap: 22px;
  }
  .front-brand .brand-dot { width: 64px; height: 64px; background: var(--gloss); }
  .front-brand .brand-name { font-size: 64px; color: var(--gloss); letter-spacing: 0; }
</style>
</head>
<body>
  <main class="stage">
    <section class="card card-back" aria-label="Business card, contact side">
      <div class="back-brand">
        <span class="brand-dot"></span>
        <span class="brand-name">Flint Studio</span>
      </div>
      <div class="person">
        <p class="person-name">Daniel Hartley</p>
        <p class="person-role">Marketing Director</p>
      </div>
      <div class="contact-row">
        <div class="contact-group">
          <p>0412 555 018</p>
          <p>03 9555 0142</p>
        </div>
        <div class="contact-group">
          <p>dhartley@flintstudio.com</p>
          <p>@dhartley</p>
        </div>
        <div class="contact-group">
          <p>flintstudio.com</p>
        </div>
      </div>
    </section>

    <section class="card card-front" aria-label="Business card, brand side">
      <div class="front-brand">
        <span class="brand-dot"></span>
        <span class="brand-name">Flint Studio</span>
      </div>
    </section>
  </main>
</body>
</html>
```